International drinks company needs a logo and powerpoint template for an IT tool being developed for

The tool name is "Northfield Vantage Hub". We are looking for a logo for the tool, and also power point templates we can use for all our presentation material. The logo will be used on the internal communication materials, launch materials, and the internal website.
The tool brings together multiple data sets and will allow our end users to drive insight that will improve business performance. This will be achieved through improved visibility of our data and investigating data relationships across data sets.
The final design should communicate simplicity from a previously complex world.

Target Market(s)

Professional

Industry/Entity Type

It Company

Logo Text

NV Vantage Hub

Font styles to use
Sans Serif

Requirements
Should not have
• cartoons, feature people under the age of 18

```html
<!DOCTYPE html>
<html lang="en">
<head>
<meta charset="utf-8">
<title>Northfield Vantage Hub — Identity and Slide Templates</title>
<link rel="stylesheet" href="https://fonts.googleapis.com/css2?family=Montserrat:wght@700&family=Questrial&display=swap">
<style>
  :root {
    --brand-red: #9c0a12;
    --ink: #000000;
    --paper: #ffffff;
    --board: #e6e6e6;
    --label: #222222;
    --body-text: #1a1a1a;
    --faint: rgba(156, 10, 18, 0.13);
  }
  * { box-sizing: border-box; margin: 0; padding: 0; }
  html, body { width: 806px; height: 1200px; overflow: hidden; }
  body {
    position: relative;
    background: var(--board);
    font-family: "Questrial", "Century Gothic", sans-serif;
    color: var(--ink);
  }

  .identity { position: absolute; left: 0; top: 0; width: 806px; height: 314px; background: var(--paper); }

  .logo { position: absolute; display: flex; flex-direction: column; align-items: center; }
  .logo .mark { background: var(--ink); flex: none; }
  .logo .name { color: var(--brand-red); white-space: nowrap; text-transform: uppercase; line-height: 1; }

  .logo--hero { left: 0; width: 806px; top: 69px; gap: 17px; }
  .logo--hero .mark { width: 101px; height: 101px; }
  .logo--hero .name { font-size: 30px; }

  .logo--mini { left: 3px; width: 100px; top: 255px; gap: 6px; }
  .logo--mini .mark { width: 29px; height: 29px; }
  .logo--mini .name { font-size: 7.5px; }

  .option-label { position: absolute; font-size: 14px; color: var(--label); }

  .slide { position: absolute; width: 331px; height: 251px; background: var(--paper); overflow: hidden; }
  .col-left { left: 56px; }
  .col-right { left: 423px; }
  .row-cover { top: 355px; }
  .row-middle { top: 638px; }
  .row-last { top: 926px; }

  .title-band { position: absolute; color: var(--paper); text-transform: uppercase; line-height: 1; }
  .title-band .title { font-size: 16px; }
  .title-band .subtitle { font-size: 8px; margin-top: 4px; }

  .cover-one .logo { left: 0; width: 331px; top: 60px; gap: 9px; }
  .cover-one .logo .mark { width: 44px; height: 44px; }
  .cover-one .logo .name { font-size: 12px; }
  .cover-one .title-band { left: 0; top: 169px; width: 331px; height: 44px; background: var(--brand-red); text-align: center; padding-top: 9px; }

  .cover-two .title-band { left: 1px; top: 112px; width: 193px; height: 43px; background: var(--ink); padding: 9px 0 0 13px; }
  .cover-two .logo { right: 8px; top: 182px; gap: 8px; }
  .cover-two .logo .mark { width: 33px; height: 33px; }
  .cover-two .logo .name { font-size: 9px; }

  .heading { position: absolute; left: 21px; top: 25px; font-family: "Montserrat", "Arial", sans-serif; font-weight: 700; font-size: 19px; letter-spacing: 0.02em; }
  .body-copy { position: absolute; left: 23px; top: 68px; width: 290px; font-size: 7.8px; line-height: 9.7px; letter-spacing: 0.15px; color: var(--body-text); }
  .body-copy p + p { margin-top: 9.7px; }
  .backdrop-square { position: absolute; left: 114px; top: 75px; width: 105px; height: 105px; background: var(--faint); }

  .topic-bar { position: absolute; display: flex; align-items: center; justify-content: space-between; color: var(--paper); font-size: 8px; padding: 0 6px; }
  .topic-bar svg { width: 8px; height: 10px; flex: none; }
  .topic-bar svg path { fill: none; stroke: var(--paper); stroke-width: 2; }
  .middle-one .tab { position: absolute; left: 0; top: 221px; width: 32px; height: 17px; background: var(--brand-red); }
  .middle-one .tab-mark { position: absolute; left: 41px; top: 213px; width: 29px; height: 29px; background: var(--ink); }
  .middle-one .topic-bar { left: 80px; top: 221px; width: 251px; height: 17px; background: var(--ink); }
  .middle-two .topic-bar { left: 0; top: 227px; width: 331px; height: 24px; background: var(--brand-red); padding: 0 10px; font-weight: 700; font-size: 8.5px; }
  .middle-two .topic-bar svg { width: 10px; height: 12px; }

  .closing .band-top, .closing .band-bottom { position: absolute; left: 0; width: 331px; height: 82px; }
  .closing .band-top { top: 0; }
  .closing .band-bottom { top: 168px; color: var(--paper); text-align: center; text-transform: uppercase; padding-top: 27px; line-height: 1; }
  .closing .band-bottom .thanks { font-size: 18px; }
  .closing .band-bottom .thanks-sub { font-size: 8.5px; margin-top: 4px; }
  .closing .logo { left: 0; width: 331px; top: 96px; gap: 8px; }
  .closing .logo .mark { width: 38px; height: 38px; }
  .closing .logo .name { font-size: 11px; }
  .closing-red .band-top, .closing-red .band-bottom { background: var(--brand-red); }
  .closing-black .band-top, .closing-black .band-bottom { background: var(--ink); }
</style>
</head>
<body>

<section class="identity">
  <div class="logo logo--hero"><span class="mark"></span><span class="name">Northfield Vantage Hub</span></div>
  <div class="logo logo--mini"><span class="mark"></span><span class="name">Northfield Vantage Hub</span></div>
</section>

<div class="option-label" style="left:56px; top:334px;">Slide Cover Option #1</div>
<div class="option-label" style="left:423px; top:334px;">Slide Cover Option #2</div>

<div class="slide col-left row-cover cover-one">
  <div class="logo"><span class="mark"></span><span class="name">Northfield Vantage Hub</span></div>
  <div class="title-band"><div class="title">Presentation Title</div><div class="subtitle">Sub Hedline Goes Here</div></div>
</div>

<div class="slide col-right row-cover cover-two">
  <div class="title-band"><div class="title">Presentation Title</div><div class="subtitle">Sub Hedline Goes Here</div></div>
  <div class="logo"><span class="mark"></span><span class="name">Northfield Vantage Hub</span></div>
</div>

<div class="option-label" style="left:56px; top:617px;">Middle Slides Option #1</div>
<div class="option-label" style="left:423px; top:617px;">Middle Slides Option #2</div>

<div class="slide col-left row-middle middle-one">
  <div class="backdrop-square"></div>
  <div class="heading">HEADING</div>
  <div class="body-copy">
    <p>Lorem Ipsum is simply dummy text of the printing and typesetting industry. Lorem Ipsum has been the industry's standard dummy text ever since the 1500s, when an unknown printer took a galley of type and scrambled it to make a type specimen book. It has survived not only five centuries, but also the leap into electronic typesetting, remaining essentially unchanged. It was popularised in the 1960s with the release of Letterline sheets containing Lorem Ipsum passages, and more recently with desktop publishing software like Pressmark Studio including versions of Lorem Ipsum.</p>
    <p>Lorem Ipsum is simply dummy text of the printing and typesetting industry. Lorem Ipsum has been the industry's standard dummy text ever since the 1500s, when an unknown printer took a galley of type and scrambled it to make a type specimen book.</p>
  </div>
  <div class="tab"></div>
  <div class="tab-mark"></div>
  <div class="topic-bar">
    <svg viewBox="0 0 8 10"><path d="M6 1 L2 5 L6 9"/></svg>
    <span>Topic Name Goes Here Till It Ends</span>
    <svg viewBox="0 0 8 10"><path d="M2 1 L6 5 L2 9"/></svg>
  </div>
</div>

<div class="slide col-right row-middle middle-two">
  <div class="backdrop-square"></div>
  <div class="heading">HEADING</div>
  <div class="body-copy">
    <p>Lorem Ipsum is simply dummy text of the printing and typesetting industry. Lorem Ipsum has been the industry's standard dummy text ever since the 1500s, when an unknown printer took a galley of type and scrambled it to make a type specimen book. It has survived not only five centuries, but also the leap into electronic typesetting, remaining essentially unchanged. It was popularised in the 1960s with the release of Letterline sheets containing Lorem Ipsum passages, and more recently with desktop publishing software like Pressmark Studio including versions of Lorem Ipsum.</p>
    <p>Lorem Ipsum is simply dummy text of the printing and typesetting industry. Lorem Ipsum has been the industry's standard dummy text ever since the 1500s, when an unknown printer took a galley of type and scrambled it to make a type specimen book.</p>
  </div>
  <div class="topic-bar">
    <svg viewBox="0 0 8 10"><path d="M6 1 L2 5 L6 9"/></svg>
    <span>Topic Name Goes Here Till It Ends</span>
    <svg viewBox="0 0 8 10"><path d="M2 1 L6 5 L2 9"/></svg>
  </div>
</div>

<div class="option-label" style="left:56px; top:905px;">Last Slide Option #1</div>
<div class="option-label" style="left:423px; top:905px;">Last Slide Option #2</div>

<div class="slide col-left row-last closing closing-red">
  <div class="band-top"></div>
  <div class="logo"><span class="mark"></span><span class="name">Northfield Vantage Hub</span></div>
  <div class="band-bottom"><div class="thanks">Thank You</div><div class="thanks-sub">For Your Attention</div></div>
</div>

<div class="slide col-right row-last closing closing-black">
  <div class="band-top"></div>
  <div class="logo"><span class="mark"></span><span class="name">Northfield Vantage Hub</span></div>
  <div class="band-bottom"><div class="thanks">Thank You</div><div class="thanks-sub">For Your Attention</div></div>
</div>

</body>
</html>
```